New Podcast focussing on non-mainstream interventions for guidance needs podcast art

I need an exquisite piece of podcast art work for the launch of my new podcast 'Past the Hollow'. This podcast explores unorthodox, esoteric and unconventional methods to find peace, clarity and direction in life. Topics include family Constellations Systems, Psychedelics, Equine Therapy and Floatation to name a few. A teaser has been posted on Brevlo with a strong response. The audience is primarily midlifers or those in a career/personal crisis of direction. It's meant to comfort, inform and empower and offer other ways rather than mainstream to work out what to do with your life. The file shared with you shows the pic used on Brevlo as it's illustrating the idea of illumination. You can use it or not, and whilst I am ex-Military, I don't want the cover to convey an overly military influence. I'd like 'Past the Hollow' to feature on the art work and my name, Margot Pennick. I'd like inspiration, creativity, and the idea of hope conveyed as well as clarity and courage. Whilst the podcast is about finding your direction please do no use compass images or cross road images as that is too obvious.
Hope that all helps. Looking forward to your ideas.

```html
<!DOCTYPE html>
<html lang="en">
<head>
<meta charset="utf-8">
<title>Past the Hollow — Podcast Cover</title>
<link rel="stylesheet" href="https://fonts.googleapis.com/css2?family=Montserrat:wght@200;300&display=swap">
<style>
  :root {
    --tone-dusk: #8a76a8;
    --tone-rose: #e0607e;
    --tone-amber: #ef7a4e;
    --tone-plum: #7e4a82;
    --tone-night: #2a1e3e;
    --title-ink: rgba(255, 236, 255, 0.74);
    --label-ink: #ffffff;
  }
  html, body {
    margin: 0;
    padding: 0;
    width: 1200px;
    height: 1200px;
    overflow: hidden;
    background: var(--tone-night);
  }
  .cover {
    position: relative;
    width: 1200px;
    height: 1200px;
    overflow: hidden;
    font-family: "Montserrat", "Helvetica Neue", Arial, sans-serif;
  }
  .cover__scene {
    position: absolute;
    inset: 0;
    background: linear-gradient(172deg,
      var(--tone-dusk) 0%,
      var(--tone-rose) 34%,
      var(--tone-amber) 56%,
      var(--tone-plum) 80%,
      var(--tone-night) 100%);
  }
  .cover__label {
    position: absolute;
    left: 0;
    right: 0;
    margin: 0;
    text-align: center;
    color: var(--label-ink);
    font-weight: 300;
    line-height: 1;
    text-transform: uppercase;
    white-space: nowrap;
  }
  .cover__kicker {
    top: 94px;
    font-size: 70px;
    letter-spacing: 0.54em;
    padding-left: calc(0.54em + 22px);
  }
  .cover__host {
    top: 1049px;
    font-size: 67px;
    letter-spacing: 0.45em;
    padding-left: calc(0.45em + 26px);
  }
  .cover__title {
    position: absolute;
    left: 53px;
    top: 251px;
    margin: 0;
    color: var(--title-ink);
    font-weight: 300;
    font-size: 236px;
    line-height: 228px;
    letter-spacing: 0.01em;
    text-transform: uppercase;
    white-space: nowrap;
  }
  .cover__title-line {
    display: block;
  }
</style>
</head>
<body>
  <main class="cover">
    <div class="cover__scene" role="img" aria-label="Illustration area: sunset landscape with a lone walker on a country road"></div>
    <p class="cover__label cover__kicker">Podcast</p>
    <h1 class="cover__title">
      <span class="cover__title-line">Past</span>
      <span class="cover__title-line">The</span>
      <span class="cover__title-line">Hollow</span>
    </h1>
    <p class="cover__label cover__host">Margot Pennick</p>
  </main>
</body>
</html>
```